Candle company needs a label for candle

Looking for a designer to create my candle label. I am going to attach a few pictures of my vision for the label as well as my Company Logo and jar I have puchased. I'm going for the modern rustic feel but you are the designer and have full trust in your abilities. The label is going to be printed on Kraft paper (2x3) so looking for the font to be black. The candle label MUST include the following information:
Wick Harbor Co.
NO. 01: Eucalyptus + Spearmint
Handmade In NJ
Soy Wax
9oz

Industry/Entity Type

Candle Industry

Colors

Designer to choose colors to be used in the design.

Requirements
Should not have
• Any images

```html
<!DOCTYPE html>
<html lang="en">
<head>
<meta charset="utf-8">
<title>Wick Harbor Co. — No. 01 Eucalyptus + Spearmint Label</title>
<link rel="stylesheet" href="https://fonts.googleapis.com/css2?family=Josefin+Sans:wght@300&family=Oswald:wght@400&family=Courier+Prime:wght@400;700&display=swap">
<style>
  :root {
    --canvas: #ffffff;
    --kraft: #b7aa8f;
    --kraft-light: #c2b69c;
    --ink: #1f1d1a;
    --ink-soft: #2b2824;
  }
  * { margin: 0; padding: 0; box-sizing: border-box; }
  html, body {
    width: 1200px;
    height: 1200px;
    overflow: hidden;
    background: var(--canvas);
  }
  .label {
    position: absolute;
    left: 100px;
    top: 256px;
    width: 1000px;
    height: 688px;
    background: radial-gradient(ellipse at 50% 45%, var(--kraft-light), var(--kraft));
    color: var(--ink);
  }
  .brand {
    position: absolute;
    left: 0;
    right: 0;
    top: 110px;
    text-align: center;
    font-family: "Josefin Sans", sans-serif;
    font-weight: 300;
    font-size: 54px;
    letter-spacing: 0.16em;
    line-height: 1.2;
    color: var(--ink);
  }
  .scent-name {
    position: absolute;
    left: 0;
    right: 0;
    top: 368px;
    text-align: center;
    font-family: "Oswald", sans-serif;
    font-weight: 400;
    font-size: 74px;
    letter-spacing: 0.02em;
    line-height: 1;
    color: var(--ink);
    text-transform: uppercase;
  }
  .rule-dashed {
    position: absolute;
    left: 140px;
    width: 714px;
    border-top: 2px dashed var(--ink-soft);
  }
  .rule-dashed.top { top: 507px; }
  .rule-dashed.bottom { top: 650px; }
  .number {
    position: absolute;
    left: 158px;
    top: 552px;
    font-family: "Courier Prime", monospace;
    font-weight: 700;
    font-size: 50px;
    line-height: 1;
    color: var(--ink-soft);
  }
  .divider {
    position: absolute;
    left: 386px;
    top: 535px;
    height: 108px;
    border-left: 2px solid var(--ink-soft);
  }
  .detail {
    position: absolute;
    left: 446px;
    font-family: "Courier Prime", monospace;
    font-weight: 400;
    font-size: 28px;
    line-height: 1;
    color: var(--ink-soft);
  }
  .detail.origin { top: 540px; }
  .detail.spec { top: 610px; }
  .detail-rule {
    position: absolute;
    left: 446px;
    top: 580px;
    width: 410px;
    border-top: 2px solid var(--ink-soft);
  }
</style>
</head>
<body>
  <div class="label">
    <div class="brand">WICK HARBOR CO.</div>
    <h1 class="scent-name">Eucalyptus + Spearmint</h1>
    <div class="rule-dashed top"></div>
    <div class="number">NO. 01</div>
    <div class="divider"></div>
    <p class="detail origin">Handmade In NJ</p>
    <div class="detail-rule"></div>
    <p class="detail spec">100% Soy Wax | 9oz</p>
    <div class="rule-dashed bottom"></div>
  </div>
</body>
</html>
```